Fitness business need 3x3 card to promote 6wk boot camp nutrition challenge

Hi, we're looking for someone to make our current card look better and more modern. We want to keep the text the same, but we want a better design. We also want to keep the woman on the front of the card. The card is for both men and women so we want it to feel inclusive and bright. The idea is to make the card look more modern. We want some pops of color. The main feature is to promote the pricing on the back of the card. It would be nice if that continues to look like a coupon or if it stands out with a bright color or background.

Target Market(s)

Men and women looking to get in shape

Industry/Entity Type

Fitness

Font styles to use
Serif
Sans Serif

Colors
3176b5
0255a3
33a6d7
f37122
ec1f27

Requirements
Must have
• front and back, use pic of women provided

```html
<!DOCTYPE html>
<html lang="en">
<head>
<meta charset="utf-8">
<title>Boot Camp Challenge Card – Front and Back</title>
<link rel="stylesheet" href="https://fonts.googleapis.com/css2?family=Oswald:wght@400;500;700&family=Montserrat:wght@600;700&family=Open+Sans:wght@400;600;700&display=swap">
<style>
  :root {
    --canvas: #d6d6d6;
    --card-black: #0d0d0e;
    --card-charcoal: #1c1c1f;
    --brand-red: #ec1f27;
    --deep-red: #b5121a;
    --accent-orange: #f37122;
    --silver-light: #f4f4f4;
    --silver-mid: #b9b9b9;
    --silver-dark: #6e6e6e;
    --text-light: #ffffff;
    --text-soft: #e2e2e2;
    --text-dark: #1a1a1a;
  }
  * { margin: 0; padding: 0; box-sizing: border-box; }
  html, body { width: 1200px; height: 1200px; overflow: hidden; }
  body { background: var(--canvas); position: relative; }
  .card { position: absolute; width: 532px; height: 532px; }
  .card svg { display: block; width: 100%; height: 100%; }
  .card--front { left: 210px; top: 46px; }
  .card--back { left: 476px; top: 622px; }

  .display { font-family: "Oswald", "Arial Narrow", sans-serif; font-weight: 700; }
  .display-regular { font-family: "Oswald", "Arial Narrow", sans-serif; font-weight: 500; }
  .date-line { font-family: "Montserrat", Arial, sans-serif; font-weight: 600; }
  .body-copy { font-family: "Open Sans", Arial, sans-serif; font-weight: 700; }
  .contact-copy { font-family: "Open Sans", Arial, sans-serif; font-weight: 400; }
  .logo-name { font-family: "Open Sans", Arial, sans-serif; font-weight: 600; }
</style>
</head>
<body>

<!-- FRONT -->
<div class="card card--front">
  <svg viewBox="0 0 665 665" xmlns="http://www.w3.org/2000/svg">
    <defs>
      <linearGradient id="front-bg" x1="0" y1="0" x2="1" y2="1">
        <stop offset="0" stop-color="var(--card-charcoal)"/>
        <stop offset="1" stop-color="var(--card-black)"/>
      </linearGradient>
      <linearGradient id="front-silver" x1="0" y1="0" x2="1" y2="0">
        <stop offset="0" stop-color="var(--silver-dark)"/>
        <stop offset="0.5" stop-color="var(--silver-light)"/>
        <stop offset="1" stop-color="var(--silver-mid)"/>
      </linearGradient>
      <linearGradient id="front-photo-top" x1="0" y1="0" x2="1" y2="1">
        <stop offset="0" stop-color="#cfcfcf"/>
        <stop offset="0.6" stop-color="#9a9a9a"/>
        <stop offset="1" stop-color="#5c5c5c"/>
      </linearGradient>
      <linearGradient id="front-photo-bottom" x1="0" y1="0" x2="1" y2="0">
        <stop offset="0" stop-color="#3a3a3a"/>
        <stop offset="0.35" stop-color="#e7e7e7"/>
        <stop offset="0.7" stop-color="#c9a38a"/>
        <stop offset="1" stop-color="#f2f2f2"/>
      </linearGradient>
      <linearGradient id="title-silver" x1="0" y1="0" x2="0" y2="1">
        <stop offset="0" stop-color="#ffffff"/>
        <stop offset="0.5" stop-color="#bdbdbd"/>
        <stop offset="1" stop-color="#8a8a8a"/>
      </linearGradient>
    </defs>

    <rect class="card-base" width="665" height="665" fill="url(#front-bg)"/>

    <!-- top photo area -->
    <path class="swoosh" d="M490,0 L465,0 C420,160 300,300 0,350 L0,362 C320,318 440,170 490,0 Z" fill="url(#front-silver)"/>
    <path d="M0,0 L462,0 C418,158 300,296 0,346 Z" fill="url(#front-photo-top)" role="img" aria-label="Black and white photo of a woman sitting on the floor beside a medicine ball"/>

    <!-- logo -->
    <circle cx="569" cy="94" r="46" fill="none" stroke="var(--text-light)" stroke-width="4"/>
    <text class="logo-name" x="569" y="90" font-size="21" fill="var(--text-light)" text-anchor="middle">YOUR</text>
    <text class="logo-name" x="569" y="116" font-size="21" fill="var(--text-light)" text-anchor="middle">LOGO</text>

    <!-- title -->
    <text class="display" x="410" y="228" font-size="54" textLength="224" lengthAdjust="spacingAndGlyphs" fill="var(--brand-red)">BOOT CAMP</text>
    <text class="display" x="412" y="331" font-size="110" textLength="207" lengthAdjust="spacingAndGlyphs" fill="url(#title-silver)">TITLE</text>

    <!-- challenge band -->
    <path d="M0,360 L580,360 L555,418 L0,418 Z" fill="var(--brand-red)"/>
    <path d="M598,360 L624,360 L599,418 L573,418 Z" fill="var(--brand-red)"/>
    <path d="M634,360 L660,360 L635,418 L609,418 Z" fill="var(--brand-red)"/>
    <text class="display-regular" x="22" y="405" font-size="38" textLength="533" lengthAdjust="spacingAndGlyphs" fill="var(--text-light)">6 WEEK FITNESS &amp; NUTRITION CHALLENGE</text>

    <text class="date-line" x="22" y="461" font-size="30" textLength="465" lengthAdjust="spacingAndGlyphs" fill="var(--text-soft)">October 2nd-November 11th</text>

    <!-- bottom photo area -->
    <path class="swoosh" d="M0,648 C200,520 450,480 665,492 L665,504 C450,494 210,530 0,665 Z" fill="url(#front-silver)"/>
    <path d="M0,665 C210,532 450,498 665,506 L665,665 Z" fill="url(#front-photo-bottom)" role="img" aria-label="Photo of dumbbells and a man and woman lifting weights in a bright gym"/>

    <!-- url bar -->
    <path d="M110,628 L665,628 L665,665 L80,665 Z" fill="var(--brand-red)"/>
    <text class="date-line" x="224" y="653" font-size="18" textLength="399" lengthAdjust="spacingAndGlyphs" fill="var(--text-light)">www.YourGymURL.com/landingpage</text>
  </svg>
</div>

<!-- BACK -->
<div class="card card--back">
  <svg viewBox="0 0 665 665" xmlns="http://www.w3.org/2000/svg">
    <defs>
      <linearGradient id="back-bg" x1="0" y1="0" x2="1" y2="1">
        <stop offset="0" stop-color="var(--card-charcoal)"/>
        <stop offset="1" stop-color="var(--card-black)"/>
      </linearGradient>
      <linearGradient id="back-silver" x1="0" y1="0" x2="1" y2="0">
        <stop offset="0" stop-color="var(--silver-dark)"/>
        <stop offset="0.5" stop-color="var(--silver-light)"/>
        <stop offset="1" stop-color="var(--silver-mid)"/>
      </linearGradient>
      <linearGradient id="back-photo-top" x1="0" y1="0" x2="1" y2="1">
        <stop offset="0" stop-color="#a88f7c"/>
        <stop offset="0.5" stop-color="#6b6160"/>
        <stop offset="1" stop-color="#3c3a3c"/>
      </linearGradient>
      <linearGradient id="back-photo-red" x1="0" y1="0" x2="1" y2="1">
        <stop offset="0" stop-color="var(--brand-red)"/>
        <stop offset="0.6" stop-color="var(--deep-red)"/>
        <stop offset="1" stop-color="var(--brand-red)"/>
      </linearGradient>
      <linearGradient id="coupon-fill" x1="0" y1="0" x2="0" y2="1">
        <stop offset="0" stop-color="#ffffff"/>
        <stop offset="0.55" stop-color="#e4e4e4"/>
        <stop offset="1" stop-color="#a9a9a9"/>
      </linearGradient>
    </defs>

    <rect class="card-base" width="665" height="665" fill="url(#back-bg)"/>

    <!-- top photo area -->
    <path class="swoosh" d="M430,0 L402,0 C360,140 240,250 0,282 L0,294 C262,268 390,150 430,0 Z" fill="url(#back-silver)"/>
    <path d="M0,0 L398,0 C356,138 238,246 0,278 Z" fill="url(#back-photo-top)" role="img" aria-label="Photo of a group class doing push-ups in a gym"/>

    <!-- logo -->
    <circle cx="580" cy="84" r="44" fill="none" stroke="var(--text-light)" stroke-width="4"/>
    <text class="logo-name" x="580" y="80" font-size="20" fill="var(--text-light)" text-anchor="middle">YOUR</text>
    <text class="logo-name" x="580" y="104" font-size="20" fill="var(--text-light)" text-anchor="middle">LOGO</text>

    <!-- title block -->
    <text class="display" x="363" y="184" font-size="40" textLength="267" lengthAdjust="spacingAndGlyphs" fill="var(--brand-red)">BOOT CAMP TITLE</text>
    <text class="display-regular" x="360" y="234" font-size="44" textLength="272" lengthAdjust="spacingAndGlyphs" fill="var(--text-light)">6 WEEK FITNESS &amp;</text>
    <text class="display-regular" x="360" y="274" font-size="36" textLength="272" lengthAdjust="spacingAndGlyphs" fill="var(--text-light)">NUTRITION CHALLENGE</text>

    <!-- headline band -->
    <path d="M0,296 L540,296 L515,355 L0,355 Z" fill="var(--brand-red)"/>
    <path d="M556,296 L584,296 L559,355 L531,355 Z" fill="var(--brand-red)"/>
    <path d="M596,296 L624,296 L599,355 L571,355 Z" fill="var(--brand-red)"/>
    <text class="display-regular" x="25" y="340" font-size="38" textLength="462" lengthAdjust="spacingAndGlyphs" fill="var(--text-light)">NO BARBELLS ! NO HEAVY WEIGHTS !</text>

    <!-- body copy -->
    <text class="body-copy" x="23" y="382" font-size="16" textLength="548" lengthAdjust="spacingAndGlyphs" fill="var(--text-light)">Burn fat, build muscle &amp; have fun! Tons of classes led by world-class</text>
    <text class="body-copy" x="23" y="404" font-size="16" textLength="484" lengthAdjust="spacingAndGlyphs" fill="var(--text-light)">coaches. Personalized nutrition planning, prizes, and more!</text>
    <text class="body-copy" x="23" y="433" font-size="21" textLength="177" lengthAdjust="spacingAndGlyphs" fill="var(--accent-orange)">SIGN UP TODAY!</text>

    <!-- price coupon -->
    <rect x="25" y="455" width="235" height="128" rx="18" fill="#2b2b2b" stroke="#9a9a9a" stroke-width="2" stroke-dasharray="3 3"/>
    <rect x="33" y="463" width="219" height="112" rx="14" fill="url(#coupon-fill)"/>
    <text class="display" x="87" y="532" font-size="62" textLength="116" lengthAdjust="spacingAndGlyphs" fill="var(--brand-red)">$249</text>
    <text class="body-copy" x="43" y="560" font-size="20" textLength="202" lengthAdjust="spacingAndGlyphs" fill="var(--text-dark)">6 WEEKS FOR ONLY</text>

    <!-- bottom red photo area -->
    <path class="swoosh" d="M200,665 C330,520 480,420 665,396 L665,408 C490,432 350,528 222,665 Z" fill="url(#back-silver)"/>
    <path d="M224,665 C352,530 492,434 665,410 L665,665 Z" fill="url(#back-photo-red)" role="img" aria-label="Red-toned photo of a person lifting a dumbbell"/>

    <!-- contact logo -->
    <circle cx="588" cy="477" r="31" fill="none" stroke="var(--text-light)" stroke-width="3"/>
    <text class="logo-name" x="543" y="529" font-size="16" textLength="92" lengthAdjust="spacingAndGlyphs" fill="var(--text-light)">YOUR LOGO</text>

    <!-- contact details -->
    <text class="contact-copy" x="478" y="570" font-size="19" textLength="135" lengthAdjust="spacingAndGlyphs" fill="var(--text-light)">17,Street Name</text>
    <text class="contact-copy" x="412" y="592" font-size="19" textLength="201" lengthAdjust="spacingAndGlyphs" fill="var(--text-light)">City name, State 10003</text>
    <text class="contact-copy" x="482" y="617" font-size="19" textLength="131" lengthAdjust="spacingAndGlyphs" fill="var(--text-light)">(555) 555-5555</text>
    <text class="contact-copy" x="348" y="641" font-size="14" textLength="265" lengthAdjust="spacingAndGlyphs" fill="var(--text-light)">www.YourGymURL.com/landingpage</text>

    <!-- icons -->
    <g class="icon-pin" fill="var(--text-light)">
      <path d="M627,556 a6,6 0 0 1 6,6 c0,5 -6,11 -6,11 c0,0 -6,-6 -6,-11 a6,6 0 0 1 6,-6 Z"/>
      <circle cx="627" cy="562" r="2.2" fill="var(--brand-red)"/>
    </g>
    <g class="icon-phone">
      <circle cx="627" cy="611" r="6" fill="var(--text-light)"/>
      <path d="M624,608 q0,5 5,6" stroke="var(--brand-red)" stroke-width="1.8" fill="none"/>
    </g>
    <g class="icon-web" fill="none" stroke="var(--text-light)" stroke-width="1.5">
      <circle cx="627" cy="636" r="6"/>
      <path d="M621,636 h12 M627,630 v12"/>
    </g>
  </svg>
</div>

</body>
</html>
```